K SPIRES Business Card Design

Need a business card design for K Spires, we're a tower company - our main scope of work is to upgrade cellular sites: swap antennas, install new coax, fiber, replace mounts, etc. Mostly tower work.

would like to see a sharp business card design with our logo either on background or with tower image on the background - something describing our field not only in words but in images.

Target Market(s)

USA

Industry/Entity Type

Business

Contact Information for Business Card

Tarik Bensalem
Operations Manager
K Spires LLC

cell 404-555-0193
tarik@k-spires-example.com

2315 Larkfield Commerce Pkwy, Suite B
Norcross, GA, 30092

Requirements
Must have
• some tower related design
Nice to have
• some tower or cellular antennas on the background, if possible to compliment our logo...

```html
<!DOCTYPE html>
<html lang="en">
<head>
<meta charset="utf-8">
<title>K Spires – Business Card</title>
<link href="https://fonts.googleapis.com/css2?family=Montserrat:wght@400;500;600&display=swap" rel="stylesheet">
<style>
  :root{
    --stage:#e9e9ea;
    --card-white:#ffffff;
    --brand-blue:#2e2a8c;
    --brand-green:#2f9a3c;
    --ink-light:#ffffff;
    --ink-soft:#d9d8f2;
  }
  html,body{margin:0;padding:0;width:1200px;height:718px;overflow:hidden;background:var(--stage);}
  body{font-family:"Montserrat",Arial,sans-serif;}
  .card{
    position:absolute;left:150px;top:102px;width:900px;height:514px;
    background:var(--card-white);overflow:hidden;
    box-shadow:0 10px 30px rgba(0,0,0,.12);
  }
  .card__shape{position:absolute;inset:0;}
  .card__details{position:absolute;left:54px;top:52px;width:330px;color:var(--ink-light);}
  .person__name{margin:0;font-size:27px;font-weight:500;letter-spacing:2px;text-transform:uppercase;white-space:nowrap;}
  .person__title{margin:6px 0 0;font-size:16px;color:var(--ink-soft);}
  .address{margin:70px 0 0;font-size:15px;line-height:1.55;}
  .contacts{list-style:none;margin:52px 0 0;padding:0;font-size:14px;}
  .contacts li{display:flex;align-items:center;gap:12px;margin-bottom:10px;white-space:nowrap;}
  .contacts svg{width:16px;height:16px;fill:var(--ink-light);flex:none;}
  .brand{
    position:absolute;left:555px;top:205px;
    font-size:58px;font-weight:600;color:var(--brand-green);letter-spacing:1px;
    display:flex;align-items:center;gap:16px;white-space:nowrap;
  }
  .brand__mark{width:22px;height:22px;border-radius:50%;background:var(--brand-green);}
</style>
</head>
<body>
  <section class="card">
    <svg class="card__shape" viewBox="0 0 900 514" aria-hidden="true">
      <path d="M0 0 H395 C300 140 470 300 430 514 H0 Z" fill="var(--brand-blue)"/>
      <path d="M412 0 C318 140 488 300 448 514" fill="none" stroke="var(--brand-green)" stroke-width="4"/>
    </svg>

    <div class="card__details">
      <h1 class="person__name">Tarik Bensalem</h1>
      <p class="person__title">Operations Manager</p>

      <p class="address">2315 Larkfield Commerce Pkwy, Suite B<br>Norcross, GA 30092</p>

      <ul class="contacts">
        <li><svg viewBox="0 0 24 24"><path d="M6.6 10.8a15 15 0 0 0 6.6 6.6l2.2-2.2c.3-.3.7-.4 1-.2 1.1.4 2.3.6 3.6.6.6 0 1 .4 1 1V20c0 .6-.4 1-1 1A17 17 0 0 1 3 4c0-.6.4-1 1-1h3.5c.6 0 1 .4 1 1 0 1.3.2 2.5.6 3.6.1.3 0 .7-.2 1z"/></svg>404-555-0193</li>
        <li><svg viewBox="0 0 24 24"><path d="M7 1h10a2 2 0 0 1 2 2v18a2 2 0 0 1-2 2H7a2 2 0 0 1-2-2V3a2 2 0 0 1 2-2zm0 3v14h10V4z"/></svg>404-555-0193</li>
        <li><svg viewBox="0 0 24 24"><path d="M2 5h20v14H2zm2 2v.5l8 5 8-5V7z"/></svg>tarik@k-spires-example.com</li>
        <li><svg viewBox="0 0 24 24"><path d="M12 2a10 10 0 1 0 0 20 10 10 0 0 0 0-20zm0 2c1 1.3 1.8 3 2 5h-4c.2-2 1-3.7 2-5zM4.3 11h3.7c.1 1.8.4 3.4 1 4.8A8 8 0 0 1 4.3 11zm5.7 0h4c-.1 2-.8 3.8-2 5.3-1.2-1.5-1.9-3.3-2-5.3zm6 0h3.7a8 8 0 0 1-4.7 4.8c.6-1.4.9-3 1-4.8z"/></svg>www.k-spires-example.com</li>
      </ul>
    </div>

    <div class="brand"><span class="brand__mark"></span>K Spires</div>
  </section>
</body>
</html>
```